New Graphic Design Project

We are working with an odd shape sign and need some creative ways to use our logo to advertise our business. This sign is on the top of our building. It is 35 inches tall and 15 feet long. We would like to use our logo (see attached) in the design. Please visit our website to get a feel for our brand and image. www.CascadeHatchetHall.com

The sign is backlit and will be printed onto plastic with vinyl.

```html
<!DOCTYPE html>
<html lang="en">
<head>
<meta charset="utf-8">
<title>Cascade Hatchet – Rooftop Sign Concepts</title>
<link href="https://fonts.googleapis.com/css2?family=Black+Ops+One&family=Oswald:wght@700&display=swap" rel="stylesheet">
<style>
  :root {
    --backdrop-light: #ececec;
    --backdrop-dark: #a9a9a9;
    --forest: #2f5a2c;
    --ink: #1c1c1c;
    --paper: #ffffff;
    --badge: #222222;
  }
  html, body {
    margin: 0;
    width: 1200px;
    height: 1000px;
    overflow: hidden;
  }
  .canvas {
    position: relative;
    width: 1200px;
    height: 1000px;
    background: radial-gradient(ellipse at 50% 45%, var(--backdrop-light) 0%, #d4d4d4 55%, var(--backdrop-dark) 100%);
    font-family: "Black Ops One", "Arial Black", sans-serif;
  }
  .sign {
    position: absolute;
    left: 68px;
    width: 1054px;
    height: 210px;
    box-shadow: 0 14px 22px rgba(0,0,0,0.35);
  }
  .sign--green { top: 238px; background: var(--forest); }
  .sign--white { top: 563px; background: var(--paper); }

  .badge {
    position: absolute;
    top: 39px;
    width: 128px;
    height: 128px;
    border-radius: 50%;
    background: var(--badge);
    display: flex;
    align-items: center;
    justify-content: center;
    text-align: center;
    color: var(--paper);
    font-size: 17px;
    line-height: 1.1;
  }
  .sign--white .badge { top: 41px; }
  .badge--left { left: 44px; }
  .badge--right { right: 26px; }

  .headline {
    position: absolute;
    left: 0;
    right: 0;
    top: 62px;
    margin: 0;
    text-align: center;
    font-size: 62px;
    font-weight: 400;
    letter-spacing: 1px;
    line-height: 1;
    color: var(--ink);
  }
  .sign--green .headline {
    -webkit-text-stroke: 6px var(--paper);
    paint-order: stroke fill;
  }
  .web {
    position: absolute;
    left: 0;
    right: 0;
    margin: 0;
    text-align: center;
    line-height: 1;
  }
  .sign--green .web {
    top: 146px;
    font-size: 25px;
    color: var(--ink);
    -webkit-text-stroke: 4px var(--paper);
    paint-order: stroke fill;
  }
  .sign--white .web {
    top: 145px;
    font-family: "Oswald", "Arial Narrow", sans-serif;
    font-weight: 700;
    font-size: 25px;
    letter-spacing: 1px;
    color: var(--forest);
  }
</style>
</head>
<body>
<main class="canvas">
  <section class="sign sign--green">
    <div class="badge badge--left">CASCADE<br>HATCHET</div>
    <h1 class="headline">CASCADE HATCHET</h1>
    <p class="web">WWW.CASCADEHATCHETHALL.COM</p>
    <div class="badge badge--right">CASCADE<br>HATCHET</div>
  </section>

  <section class="sign sign--white">
    <div class="badge badge--left">CASCADE<br>HATCHET</div>
    <h2 class="headline">CASCADE HATCHET</h2>
    <p class="web">WWW.CASCADEHATCHETHALL.COM</p>
    <div class="badge badge--right">CASCADE<br>HATCHET</div>
  </section>
</main>
</body>
</html>
```